Fernvale Business Card Design

We are looking for a fresh business card design for our new logo. We would like a business card that is unique but friendly. We are in the window coverings business offering blinds, shutters and shades for homes.

Target Market(s)

Targeting the end-consumer

Industry/Entity Type

Business

Requirements
Must have
• Must have a dedicates space for a photo of our sales person. Must contain our new logo (attached).

```html
<!DOCTYPE html>
<html lang="en">
<head>
<meta charset="utf-8">
<title>Fernvale Business Card</title>
<link rel="stylesheet" href="https://fonts.googleapis.com/css2?family=Cabin:wght@500;600&family=Lato:wght@400&family=Rosario:wght@500&display=swap">
<style>
  :root {
    --stage: #262626;
    --stage-glow: #4a4a4a;
    --slate: #65666a;
    --slate-text: #5b5c60;
    --paper: #ffffff;
    --leaf: #8cc63f;
    --rule: #b5b5b5;
    --suit: #2f3a55;
  }
  * { margin: 0; padding: 0; box-sizing: border-box; }
  html, body { width: 1189px; height: 1200px; overflow: hidden; }
  body {
    position: relative;
    background: radial-gradient(ellipse at 50% 55%, var(--stage-glow) 0%, var(--stage) 70%);
    font-family: "Lato", sans-serif;
  }
  .card {
    position: absolute;
    left: 171px;
    width: 856px;
    height: 489px;
    border-radius: 33px;
    overflow: hidden;
    box-shadow: 0 6px 14px rgba(0,0,0,0.45);
  }
  .card--front { top: 66px; background: var(--slate); }
  .card--back { top: 626px; background: var(--paper); }

  .brand { position: absolute; display: flex; align-items: center; gap: 26px; }
  .brand__square { width: 100px; height: 100px; border: 5px solid currentColor; border-radius: 10px; }
  .brand__name { font-family: "Rosario", sans-serif; font-weight: 500; font-size: 80px; line-height: 1; }
  .card--front .brand { left: 199px; top: 195px; color: var(--paper); }
  .card--back .brand { left: 54px; top: 62px; color: var(--slate-text); }

  .front__web {
    position: absolute; left: 0; right: 0; top: 400px;
    text-align: center; color: var(--paper);
    font-size: 18px; letter-spacing: 4px;
  }

  .person { position: absolute; left: 51px; top: 226px; display: flex; align-items: baseline; }
  .person__name { font-family: "Cabin", sans-serif; font-weight: 600; font-size: 31px; color: var(--slate-text); }
  .person__divider { width: 1px; height: 24px; background: var(--rule); margin: 0 22px 0 28px; align-self: center; }
  .person__role { font-size: 21px; color: var(--leaf); }
  .person__rule { position: absolute; left: 50px; top: 273px; width: 395px; height: 1px; background: var(--rule); }

  .address { position: absolute; left: 50px; top: 297px; font-size: 21px; line-height: 27px; color: var(--slate-text); }
  .contacts { position: absolute; left: 50px; top: 360px; list-style: none; }
  .contacts li { display: flex; align-items: center; height: 29px; font-size: 21px; color: var(--slate-text); }
  .contacts svg { width: 25px; height: 25px; margin-right: 10px; flex: none; }

  .portrait {
    position: absolute; left: 519px; top: 33px; width: 314px; height: 410px;
    background: linear-gradient(180deg, #e9e4e0 0%, #e9e4e0 28%, #4a5470 55%, var(--suit) 100%);
    border-radius: 120px 120px 0 0;
  }
  .bands { position: absolute; left: 0; top: 0; width: 856px; height: 489px; }
</style>
</head>
<body>

<section class="card card--front">
  <div class="brand">
    <span class="brand__square"></span>
    <span class="brand__name">Fernvale</span>
  </div>
  <p class="front__web">www.fernvaleblinds.com</p>
</section>

<section class="card card--back">
  <div class="brand">
    <span class="brand__square"></span>
    <span class="brand__name">Fernvale</span>
  </div>

  <div class="person">
    <span class="person__name">Liam Porter</span>
    <span class="person__divider"></span>
    <span class="person__role">Owner</span>
  </div>
  <div class="person__rule"></div>

  <p class="address">PO BOX 48 Harbour Lane<br>5th street Geelong</p>

  <ul class="contacts">
    <li>
      <svg viewBox="0 0 26 26" fill="none" stroke="#8cc63f" stroke-width="1.6"><circle cx="13" cy="13" r="11.5"/><rect x="9" y="6.5" width="8" height="13" rx="1.5"/><line x1="11.5" y1="17" x2="14.5" y2="17"/></svg>
      (555) 214-3870
    </li>
    <li>
      <svg viewBox="0 0 26 26" fill="none" stroke="#8cc63f" stroke-width="1.6"><circle cx="13" cy="13" r="11.5"/><rect x="7" y="8.5" width="12" height="9" fill="#8cc63f"/><polyline points="7,8.5 13,13.5 19,8.5" stroke="#fff"/></svg>
      hello@fernvaleblinds.com
    </li>
    <li>
      <svg viewBox="0 0 26 26" fill="none" stroke="#8cc63f" stroke-width="1.4"><circle cx="13" cy="13" r="11.5"/><circle cx="13" cy="13" r="6.5"/><ellipse cx="13" cy="13" rx="3" ry="6.5"/><line x1="6.5" y1="13" x2="19.5" y2="13"/></svg>
      www.fernvaleblinds.com
    </li>
  </ul>

  <div class="portrait" role="img" aria-label="Portrait photo of the sales person in a navy suit"></div>

  <svg class="bands" viewBox="0 0 856 489" aria-hidden="true">
    <polygon points="0,462 636,462 626,489 0,489" fill="var(--slate)"/>
    <polygon points="498,443 856,443 856,489 485,489" fill="var(--leaf)"/>
  </svg>
</section>

</body>
</html>
```